Wound Care Flyer

Looking for a Trifold brochure that is modern and has a high aesthetic. (Specialty services) Would like the colors to center around Black and Gold. Possibly updating the logo. Attached is the old brochure and a document about our services.

```html
<!DOCTYPE html>
<html lang="en">
<head>
<meta charset="utf-8">
<title>Cedarline Wounds Trifold</title>
<link href="https://fonts.googleapis.com/css2?family=Lato:wght@400;700&display=swap" rel="stylesheet">
<style>
:root{
  --black:#050505;
  --gold:#b39a5c;
  --gold-light:#e6d9ad;
  --gold-dark:#7d6733;
  --cream:#f2ead0;
  --white:#ffffff;
  --grey-bg:#c9c9c9;
  --ink:#111111;
}
*{margin:0;padding:0;box-sizing:border-box}
html,body{width:913px;height:1200px;overflow:hidden;background:var(--grey-bg);font-family:'Lato',sans-serif;color:var(--ink)}
.canvas{position:relative;width:913px;height:1200px}
.sheet{position:absolute;left:96px;width:720px;height:554px;overflow:hidden;background:var(--black)}
.sheet--outside{top:31px}
.sheet--inside{top:600px;height:555px;background:var(--white)}
.abs{position:absolute}
.deco{position:absolute;left:0;top:0;width:720px;height:555px}
.center{text-align:center}
.upper{text-transform:uppercase}

/* outside */
.partner-title{left:0;top:30px;width:255px;color:var(--white);font-size:17px;line-height:20px;font-weight:400}
.benefit-icon{width:41px;height:41px;border-radius:50%;background:var(--black);border:2px solid var(--gold)}
.benefit-card{left:22px;width:197px;background:var(--white);border:1px solid var(--gold-dark);padding:4px 5px;font-size:8.9px;line-height:11px;letter-spacing:-.1px;text-align:center}
.benefit-card h3{font-size:9.4px;font-weight:700;margin-bottom:1px;letter-spacing:0}
.brand-ring{border-radius:50%;border:2px solid var(--gold);background:var(--black)}
.brand-name{color:var(--gold);font-weight:400;letter-spacing:3px;text-align:center;line-height:1.1}
.contact{left:240px;width:240px;color:var(--white);text-align:center}
.contact-title{top:261px;font-size:15px;letter-spacing:.5px;font-weight:400}
.contact-lines{top:305px;font-size:13px;line-height:17px;font-weight:700}
.contact-mail{top:361px;font-size:11px;font-weight:700}
.contact-handle{top:403px;font-size:11px;font-weight:700}
.cover-title{left:540px;top:473px;width:160px;color:var(--white);font-size:23px;line-height:22px;font-weight:400}
.photo-caption{left:497px;top:285px;color:var(--white);font-size:6px;font-weight:700}

/* inside */
.about-title{left:60px;top:166px;width:160px;color:var(--white);font-size:24px;font-weight:400}
.about-name{left:0;top:220px;width:240px;font-size:20px;line-height:22px;font-weight:700}
.about-sub{left:0;top:275px;width:240px;font-size:10px;font-weight:400}
.about-body{left:27px;top:297px;width:191px;font-size:9.2px;line-height:11.2px;text-align:justify}
.about-body p+p{margin-top:11px}
.inside-head{color:var(--white);font-size:16px;line-height:20px;text-align:center;font-weight:400}
.program-box{left:261px;top:111px;width:201px;height:84px;background:var(--white);border:1px solid var(--gold-dark);font-size:9.3px;line-height:12px;padding:6px 8px;text-align:center}
.services-title{left:250px;top:213px;width:222px;font-size:14px;line-height:18.5px;text-align:center;font-weight:400}
.services-box{left:261px;top:268px;width:203px;height:240px;background:var(--black);border:1px solid var(--gold);color:var(--white);padding:5px 8px;font-size:9px;line-height:14.7px}
.services-box h4{font-weight:400;font-size:9.6px;text-align:center;margin:2px 0}
.services-box ul{list-style:none}
.services-box li{position:relative;padding-left:13px}
.services-box li::before{content:"";position:absolute;left:2px;top:5px;width:6px;height:6px;border-radius:50%;background:var(--cream)}
.care-text{left:480px;top:107px;width:220px;font-size:9.3px;line-height:12px;text-align:center}
.care-text p+p{margin-top:12px}
</style>
</head>
<body>
<div class="canvas">

  <!-- OUTSIDE -->
  <section class="sheet sheet--outside">
    <svg class="deco" viewBox="0 0 720 554" aria-hidden="true">
      <defs>
        <linearGradient id="goldSheen" x1="0" y1="0" x2="1" y2="1">
          <stop offset="0" stop-color="#7d6733"/><stop offset=".45" stop-color="#e6d9ad"/><stop offset="1" stop-color="#8a7239"/>
        </linearGradient>
        <linearGradient id="creamFade" x1="0" y1="0" x2="1" y2="0">
          <stop offset="0" stop-color="#f5efd9"/><stop offset=".7" stop-color="#efe4c0"/><stop offset="1" stop-color="#cdb679"/>
        </linearGradient>
        <linearGradient id="bandGold" x1="0" y1="0" x2="1" y2="0">
          <stop offset="0" stop-color="#8a7239"/><stop offset=".3" stop-color="#e4d6a7"/><stop offset=".6" stop-color="#b39a5c"/><stop offset="1" stop-color="#9a8142"/>
        </linearGradient>
      </defs>
      <rect x="0" y="94" width="240" height="460" fill="url(#creamFade)"/>
      <polygon points="140,94 240,94 240,554 200,554" fill="url(#goldSheen)" opacity=".55"/>
      <polygon points="374,0 480,0 480,554 460,300" fill="url(#goldSheen)"/>
      <polygon points="270,200 360,200 310,554 190,554" fill="#2a2a2a" opacity=".6"/>
      <rect x="240" y="452" width="480" height="102" fill="url(#bandGold)"/>
      <polygon points="240,452 330,452 260,554 240,554" fill="#f1e8c8" opacity=".6"/>
      <rect x="240" y="458" width="480" height="2" fill="#f3ebd0"/>
      <rect x="0" y="74" width="330" height="2" fill="url(#bandGold)"/>
      <rect x="430" y="74" width="50" height="2" fill="url(#bandGold)"/>
    </svg>

    <h2 class="abs partner-title center upper">Partner with<br>Cedarline Wounds:</h2>

    <div class="abs benefit-icon" style="left:101px;top:107px"></div>
    <div class="abs benefit-card" style="top:139px">
      <h3>ENHANCED PATIENT OUTCOMES</h3>
      <p>Our specialized expertise in advanced wound care leads to faster healing times and improved patient satisfaction.</p>
    </div>
    <div class="abs benefit-icon" style="left:101px;top:208px"></div>
    <div class="abs benefit-card" style="top:243px">
      <h3>EXTENDED REACH</h3>
      <p>Our in-home services allow your patients to receive high-quality care without the need for frequent visits, reducing the burden on your resources.</p>
    </div>
    <div class="abs benefit-icon" style="left:101px;top:318px"></div>
    <div class="abs benefit-card" style="top:355px">
      <h3>PROFESSIONAL INTEGRITY</h3>
      <p>As a trusted partner, we uphold the highest standards of care and professionalism, reflecting positively on your clinic's reputation.</p>
    </div>
    <div class="abs benefit-icon" style="left:101px;top:416px"></div>
    <div class="abs benefit-card" style="top:452px">
      <h3>SEAMLESS COLLABORATION</h3>
      <p>We maintain open communication with referring clinics, ensuring a coordinated approach to patient care.</p>
    </div>

    <div class="abs brand-ring" style="left:326px;top:49px;width:74px;height:74px"></div>
    <p class="abs brand-name" style="left:298px;top:131px;width:130px;font-size:13px">CEDARLINE<br>WOUNDS</p>

    <h3 class="abs contact contact-title">CONTACT US</h3>
    <svg class="abs" style="left:354px;top:293px" width="12" height="12" viewBox="0 0 24 24" aria-hidden="true">
      <path fill="#b39a5c" d="M6.6 10.8a15 15 0 0 0 6.6 6.6l2.2-2.2c.3-.3.7-.4 1-.2 1.1.4 2.3.6 3.6.6.6 0 1 .4 1 1V20c0 .6-.4 1-1 1A17 17 0 0 1 3 4c0-.6.4-1 1-1h3.5c.6 0 1 .4 1 1 0 1.3.2 2.5.6 3.6.1.3 0 .7-.2 1z"/>
    </svg>
    <p class="abs contact contact-lines">O: (555) 014-2260<br>F: (555) 014-2261</p>
    <svg class="abs" style="left:354px;top:347px" width="12" height="12" viewBox="0 0 24 24" aria-hidden="true">
      <circle cx="12" cy="12" r="10" fill="none" stroke="#cfcfcf" stroke-width="2"/>
      <path d="M2 12h20M12 2c3 3 3 17 0 20M12 2c-3 3-3 17 0 20" fill="none" stroke="#cfcfcf" stroke-width="1.6"/>
    </svg>
    <p class="abs contact contact-mail">hello@cedarlinewounds.com</p>
    <p class="abs contact contact-handle">@Cedarlinewounds</p>

    <div class="abs" role="img" aria-label="Portrait of the lead nurse practitioner in a white coat, hands clasped, in a clinic room"
         style="left:480px;top:0;width:240px;height:336px;background:linear-gradient(160deg,#9a9a9a,#dcdcdc 55%,#7f7f7f);clip-path:polygon(0 0,100% 0,100% 100%,94px 100%,94px 55%,0 0)"></div>
    <div class="abs" style="left:480px;top:0;width:94px;height:294px;background:linear-gradient(180deg,#8d8d8d,#bfbfbf)" role="img" aria-label="Clinic room background"></div>
    <p class="abs photo-caption">DANA MERRITT, FNP-C</p>

    <div class="abs brand-ring" style="left:556px;top:306px;width:92px;height:92px"></div>
    <p class="abs brand-name" style="left:530px;top:404px;width:150px;font-size:18px">CEDARLINE<br>WOUNDS</p>

    <h1 class="abs cover-title center upper">Advanced<br>Wound Care</h1>
  </section>

  <!-- INSIDE -->
  <section class="sheet sheet--inside">
    <svg class="deco" viewBox="0 0 720 555" aria-hidden="true">
      <defs>
        <linearGradient id="goldSheen2" x1="0" y1="0" x2="1" y2="1">
          <stop offset="0" stop-color="#efe6c6"/><stop offset=".6" stop-color="#f6f0dc"/><stop offset="1" stop-color="#d9c78f"/>
        </linearGradient>
        <linearGradient id="band2" x1="0" y1="0" x2="1" y2="0">
          <stop offset="0" stop-color="#8a7239"/><stop offset=".35" stop-color="#e8dcb0"/><stop offset=".7" stop-color="#b39a5c"/><stop offset="1" stop-color="#8a7239"/>
        </linearGradient>
      </defs>
      <rect x="240" y="0" width="480" height="95" fill="#050505"/>
      <rect x="150" y="79" width="570" height="2" fill="url(#band2)"/>
      <polygon points="130,370 480,370 480,555 90,555" fill="url(#goldSheen2)" opacity=".8"/>
      <polygon points="240,95 320,95 280,300 200,300" fill="url(#goldSheen2)" opacity=".7"/>
      <rect x="0" y="267" width="240" height="2" fill="url(#band2)"/>
      <rect x="0" y="533" width="480" height="22" fill="url(#band2)"/>
    </svg>

    <div class="abs" role="img" aria-label="Clinician in mask and gloves examining a patient's skin"
         style="left:0;top:0;width:240px;height:214px;background:linear-gradient(135deg,#6a6a6a,#d5d5d5 45%,#8a7a66);clip-path:polygon(0 0,100% 0,100% 100%,42px 100%,0 40%)"></div>
    <h2 class="abs about-title center upper">About Us</h2>
    <h2 class="abs about-name center upper">Cedarline<br>Wounds:</h2>
    <h3 class="abs about-sub center upper">Mobile Wound Care</h3>
    <div class="abs about-body">
      <p>With a focus on convenience, expertise, and compassion, we bring the highest standard of wound care directly to the patient's home. Working side-by-side with the patient's physician, our team of experienced specialists utilize cutting-edge technology and personalized treatment plans to ensure optimal healing and comfort.</p>
      <p>From thorough wound assessments to advanced therapies and ongoing support, we prioritize the well-being of our patients every step of the way. Whether it's managing chronic wounds, post-surgery recovery, we go above and beyond to provide comprehensive and compassionate care. With our concierge approach, we aim to make the healing journey as seamless and comfortable as possible, empowering our patients to live their best lives.</p>
    </div>

    <h2 class="abs inside-head upper" style="left:245px;top:34px;width:225px">Leaders in mobile<br>advanced woundcare.</h2>
    <h2 class="abs inside-head upper" style="left:480px;top:34px;width:240px">Personalized<br>care plans</h2>

    <p class="abs program-box upper">We provide a complete wound management program for our patients that includes the use of advanced treatments, the creation of care plans, and coordination of care with other clinicians.</p>
    <h3 class="abs services-title upper">Our comprehensive<br>in-home wound care<br>services include:</h3>
    <div class="abs services-box">
      <h4>ADVANCED WOUND ASSESSMENT</h4>
      <ul><li>Thorough evaluation of wound type, size, and stage to develop a tailored treatment plan.</li></ul>
      <h4 style="margin-top:9px">CUTTING-EDGE TREATMENTS</h4>
      <ul>
        <li>Utilization of the latest technologies and techniques in wound care, including:</li>
        <li>Compression</li>
        <li>Biologic Skin Substitutes</li>
        <li>Negative Pressure Wound Therapy</li>
        <li>Collagen and Advanced Dressings</li>
        <li>Surgical/ Trauma Wounds</li>
        <li>Venous/ Arterial Wounds</li>
        <li>Debridements</li>
      </ul>
    </div>

    <div class="abs care-text upper">
      <p>Customized care plans designed to meet the specific needs of each patient, ensuring optimal healing. Coordination and direction of care for other caregivers and clinicians, including home health.</p>
      <p>Patient and caregiver education providing education and support to patients and their caregivers to enhance understanding and promote self-care.</p>
    </div>

    <div class="abs" role="img" aria-label="Masked clinician in white coat with gold gloves examining a patient's face"
         style="left:480px;top:253px;width:240px;height:302px;background:linear-gradient(120deg,#5c5c5c,#cfcfcf 40%,#8c7442 75%,#3a2c1c)"></div>
  </section>

</div>
</body>
</html>
```